Washing powder bag design.

Project Description – Graphic Design Proposal for ORNE Laundry Powder Packaging
We have already explored initial design ideas internally, supported by AI-assisted tools (ChatGPT) to develop early concepts, layouts, and mockups. To support this, we have attached the bag die-cut, where graphics and text are placed as a visual guideline for the intended structure. In addition, we have included a mockup of the product series currently under development to clearly communicate the desired style, direction, and overall visual identity.
The mockup should be regarded as the design foundation for this project and as a starting point for professional refinement.
Scope of Work
We would like you to create three graphic design variants, each based on a different color direction:
1. Variant 1: In line with our current color scheme
2. Variant 2: A blue version
3. Variant 3: A green version
Design Elements to Be Preserved
The following elements must be maintained across all three variants:
• The overall style and visual expression of the mockup
• The leaf-shaped element in the bottom right corner
• The ORNE layout, including typography, positioning, and general look & feel
Summary
While the color palette may vary, the structure, style, and key design elements must remain consistent and be directly based on the attached mockup.
We look forward to seeing your creative interpretation and professional input.
Updates
We need the design to be created based on the attached die-cut file “Orne 10 kg BAG 202526”, including all text elements.
We would like the final to include both the designed die-cut file and a mockup.

```html
<!DOCTYPE html>
<html lang="da">
<head>
<meta charset="utf-8">
<title>ORNE Vaskepulver 10 kg</title>
<link rel="stylesheet" href="https://fonts.googleapis.com/css2?family=Montserrat:wght@500;700;800&family=Quicksand:wght@400;500&display=swap">
<style>
  :root {
    --stage: #f3f3f1;
    --cream: #f4efe4;
    --cream-deep: #e9e1d2;
    --seal: #dcd8d0;
    --leaf-dark: #3f5734;
    --leaf-mid: #5f7848;
    --leaf-olive: #a0ac4c;
    --band: #a3ad4f;
    --band-light: #b7c072;
    --ink: #3d5331;
    --ink-soft: #5d5f55;
    --white: #ffffff;
  }
  * { margin: 0; padding: 0; box-sizing: border-box; }
  html, body { width: 1200px; height: 784px; overflow: hidden; }
  body { background: var(--stage); font-family: "Montserrat", sans-serif; }
  .canvas { position: relative; width: 1200px; height: 784px; }

  .bag { position: absolute; left: 390px; top: 30px; display: flex; gap: 3px; }

  .front {
    position: relative; width: 340px; height: 724px;
    background: var(--cream); border-radius: 6px 6px 14px 14px; overflow: hidden;
  }
  .seal {
    height: 36px;
    background: repeating-linear-gradient(to bottom, var(--seal) 0 3px, #ece9e3 3px 6px);
  }

  .art { position: absolute; display: block; border-radius: 10px; }
  .art-top-leaves {
    left: 14px; top: 64px; width: 104px; height: 188px;
    background: linear-gradient(160deg, rgba(63,87,52,0.55), rgba(160,172,76,0.25));
  }
  .art-bottom-leaves {
    left: 224px; top: 520px; width: 100px; height: 188px; z-index: 2;
    background: linear-gradient(200deg, rgba(63,87,52,0.6), rgba(95,120,72,0.35));
  }

  .logo {
    position: absolute; left: 50%; top: 238px; transform: translateX(-50%);
    width: 168px; height: 168px; border-radius: 50%;
    background: var(--cream-deep); display: grid; place-items: center;
  }
  .logo-disc {
    width: 152px; height: 152px; border-radius: 50%;
    background: var(--leaf-olive); border: 2px solid var(--leaf-dark);
    display: grid; place-items: center;
  }
  .logo-name { font-weight: 700; font-size: 42px; letter-spacing: 1px; color: var(--leaf-dark); }

  .product-name {
    position: absolute; top: 450px; width: 100%; text-align: center;
    font-weight: 800; font-size: 27px; color: var(--ink); letter-spacing: 0.5px;
  }
  .product-sub {
    position: absolute; top: 486px; width: 100%; text-align: center;
    font-family: "Quicksand", sans-serif; font-size: 12px; color: var(--ink-soft); letter-spacing: 0.5px;
  }
  .tagline {
    position: absolute; left: 30px; top: 536px;
    font-weight: 700; font-size: 12px; line-height: 1.15; color: var(--ink); text-align: center;
  }
  .care-row {
    position: absolute; left: 18px; top: 580px; display: flex; gap: 6px;
    padding: 4px; background: var(--cream-deep); border-radius: 30px;
  }
  .care-icon {
    width: 44px; height: 44px; border-radius: 50%; border: 1.5px solid var(--leaf-dark);
    display: grid; place-items: center; background: var(--cream);
  }
  .dose { font-weight: 800; font-size: 14px; color: var(--ink); }
  .temps {
    position: absolute; left: 28px; top: 638px;
    font-weight: 700; font-size: 7px; color: var(--ink); letter-spacing: 0.2px;
  }
  .band { position: absolute; left: 0; bottom: 0; width: 340px; height: 80px; }
  .weight {
    position: absolute; left: 20px; bottom: 22px;
    font-weight: 800; font-size: 24px; color: var(--white);
  }

  .gusset {
    position: relative; width: 86px; height: 724px;
    background: var(--cream); border-radius: 6px 6px 14px 14px; overflow: hidden;
  }
  .gusset-logo {
    position: absolute; left: 12px; top: 290px; width: 62px; height: 62px; border-radius: 50%;
    border: 1px solid var(--cream-deep); display: grid; place-items: center;
  }
  .gusset-name { font-weight: 500; font-size: 14px; color: #d9ccb9; }
  .maker {
    position: absolute; left: 4px; top: 500px; width: 78px; text-align: center; color: #1d1d1b;
  }
  .maker-note { font-size: 5px; font-weight: 500; }
  .maker-name { font-size: 9px; font-weight: 800; margin: 8px 0 10px; letter-spacing: -0.2px; }
  .maker-line { font-size: 4.6px; font-weight: 500; line-height: 1.5; }
  .maker-web { margin-top: 8px; }
  .gusset-band { position: absolute; left: 0; bottom: 0; width: 86px; height: 46px; background: var(--band-light); }
  .art-gusset-leaves {
    left: 18px; bottom: 28px; width: 44px; height: 44px; border-radius: 8px;
    background: linear-gradient(180deg, rgba(63,87,52,0.6), rgba(95,120,72,0.4));
  }
</style>
</head>
<body>
<main class="canvas">
  <div class="bag">
    <section class="front" aria-label="Forside">
      <div class="seal"></div>
      <div class="art art-top-leaves" role="img" aria-label="Illustration af grøn gren med blade"></div>

      <div class="logo">
        <div class="logo-disc"><span class="logo-name">ORNE</span></div>
      </div>

      <h1 class="product-name">VASKEPULVER</h1>
      <p class="product-sub">LAUNDRY DETERGENT</p>

      <p class="tagline">LIV OG BALANCE<br>I HVERDAGEN</p>

      <div class="care-row">
        <div class="care-icon"><span class="dose">120</span></div>
        <div class="care-icon" aria-label="Maskinvask">
          <svg width="20" height="24" viewBox="0 0 26 30" fill="none" stroke="#3f5734" stroke-width="2">
            <rect x="2" y="2" width="22" height="26" rx="2"/>
            <line x1="2" y1="8" x2="24" y2="8"/>
            <circle cx="13" cy="18" r="6"/>
          </svg>
        </div>
        <div class="care-icon" aria-label="Håndvask">
          <svg width="26" height="21" viewBox="0 0 32 26" fill="none" stroke="#3f5734" stroke-width="2">
            <path d="M2 8 L6 24 H26 L30 8"/>
            <path d="M6 12 q3 -3 6 0 t6 0 t6 0 t4 0"/>
          </svg>
        </div>
      </div>
      <p class="temps">20°C | 30°C | 40°C | 60°C | 90°C</p>

      <svg class="band" viewBox="0 0 340 80" preserveAspectRatio="none" aria-hidden="true">
        <path d="M0 6 Q120 0 220 30 Q290 50 340 44 V80 H0 Z" fill="var(--band)"/>
        <path d="M0 66 Q170 74 340 70 V80 H0 Z" fill="var(--band-light)"/>
      </svg>
      <span class="weight">10Kg</span>

      <div class="art art-bottom-leaves" role="img" aria-label="Illustration af grøn plantestængel med blade"></div>
    </section>

    <aside class="gusset" aria-label="Side">
      <div class="seal"></div>
      <div class="gusset-logo"><span class="gusset-name">ORNE</span></div>

      <div class="maker">
        <p class="maker-note">Produceret i EU for</p>
        <p class="maker-name">NORDKYST ApS</p>
        <p class="maker-line">Havnegade 12<br>4500 Nykøbing, Danmark<br>Tlf: +45 20 30 40 50</p>
        <p class="maker-line maker-web">info@nordkyst.dk<br>www.nordkyst.dk</p>
      </div>

      <div class="gusset-band"></div>
      <div class="art art-gusset-leaves" role="img" aria-label="Illustration af grønne blade"></div>
    </aside>
  </div>
</main>
</body>
</html>
```